Helicopter company requires newspaper ad

"Ridgeline Aviation" is an agricultural helicopter company based in Victoria, Australia. We need an advert design for use in newspapers and also possibly social media. Our company specialises in using a helicopter for various agricultural work such as Spraying weeds ("Cropdusting"), spreading fertiliser. This advert will be targeted at farmers in our service area, Our customers are mainly dairy and cow farmers and our services are aimed at increasing their farm productivity. The final design should inform potential and existing customers about our services and the benefits of them. I will attach files of our logo and some existing advertising material for guidance. We would like the ad to feature the blue and green colours in our logo Please feel free to view our website and facebook page to see more about what we do. www.ridgelineaviation.com.au Some text we would like included Spraying: -Accurate -Time Efficient -Zero crop damage -Cost efficient Fertiliser Spreading: -Accurate, Pattern-tested equipment -Zero crop damage or wheel marks -Ability to load product out of a truck, bin or bulk bags -Cost effective, Prices from $32 per hectare depending on spread rate The final advert size should be 195 mm wide x 186 mm high Thanks :)

Farmers, Agriculture Industry

Agribusiness

Designer to choose colors to be used in the design.

• Phone number 0491 736 058
• The text included in the decription, or variations of this

```html
<!DOCTYPE html>
<html lang="en">
<head>
<meta charset="utf-8">
<title>Ridgeline Aviation – Agricultural Helicopter Services</title>
<link rel="stylesheet" href="https://fonts.googleapis.com/css2?family=Montserrat:wght@600;700&family=Open+Sans:wght@400;600;700&display=swap">
<style>
  :root {
    --brand-blue: #1176c1;
    --brand-green: #8cc63f;
    --ink: #3f3f3f;
    --paper: #ffffff;
    --sky-top: #7a8c98;
    --sky-mid: #a3b1b8;
    --field: #4f6a3c;
    --field-dark: #33472a;
  }
  * { margin: 0; padding: 0; box-sizing: border-box; }
  html, body { width: 1200px; height: 1144px; overflow: hidden; background: var(--paper); }
  .ad {
    position: relative;
    width: 1200px;
    height: 1144px;
    background: var(--paper);
    font-family: "Open Sans", Arial, sans-serif;
    color: var(--ink);
  }
  .hero {
    position: absolute;
    left: 0; top: 0;
    width: 1200px; height: 571px;
    overflow: hidden;
  }
  .hero-photo {
    position: absolute;
    inset: 0;
    background: linear-gradient(180deg, var(--sky-top) 0%, var(--sky-mid) 38%, #8e9a8c 56%, var(--field) 72%, var(--field-dark) 100%);
  }
  .band { position: absolute; left: 0; width: 1200px; display: block; }
  .band-top { top: 0; height: 19px; }
  .band-hero-bottom { top: 531px; height: 40px; }
  .band-foot { top: 1122px; height: 22px; }
  .contact {
    position: absolute;
    color: var(--paper);
    font-family: "Montserrat", Arial, sans-serif;
    font-weight: 700;
  }
  .contact-phone { left: 82px; top: 112px; font-size: 42px; letter-spacing: 4px; }
  .contact-web { left: 30px; top: 172px; font-size: 22px; letter-spacing: 2.6px; }
  .hero-title {
    position: absolute;
    left: 0; top: 362px;
    width: 1200px;
    text-align: center;
    color: var(--paper);
    font-family: "Montserrat", Arial, sans-serif;
    font-weight: 700;
    font-size: 66px;
    line-height: 82px;
    letter-spacing: 5px;
  }
  .services-label {
    position: absolute;
    left: 0; top: 622px;
    width: 1200px;
    text-align: center;
    font-weight: 600;
    font-size: 31px;
    letter-spacing: 10px;
    color: var(--ink);
  }
  .service {
    position: absolute;
    list-style: none;
    font-size: 34px;
    line-height: 54px;
    color: var(--ink);
  }
  .service-title { font-weight: 700; }
  .service-fertiliser { left: 62px; top: 696px; width: 700px; }
  .service-spraying { left: 819px; top: 696px; width: 360px; }
  .brand-name {
    position: absolute;
    left: 870px; top: 990px;
    display: flex;
    align-items: center;
    gap: 8px;
    font-family: "Open Sans", Arial, sans-serif;
    font-weight: 700;
    font-size: 19px;
    color: var(--brand-blue);
  }
  .brand-dot {
    width: 14px; height: 14px;
    border-radius: 50%;
    background: var(--brand-green);
  }
</style>
</head>
<body>
<main class="ad">
  <section class="hero">
    <div class="hero-photo" role="img" aria-label="Photograph of an agricultural helicopter spraying a green pasture on rolling hills under a cloudy sky"></div>

    <svg class="band band-top" viewBox="0 0 1200 19" preserveAspectRatio="none" aria-hidden="true">
      <rect x="0" y="0" width="1200" height="19" fill="var(--brand-green)"/>
      <polygon points="0,0 745,0 765,19 0,19" fill="var(--brand-blue)"/>
    </svg>

    <p class="contact contact-phone">0491 736 058</p>
    <p class="contact contact-web">www.ridgelineaviation.com.au</p>

    <h1 class="hero-title">AGRICULTURAL HELICOPTER<br>SERVICES</h1>

    <svg class="band band-hero-bottom" viewBox="0 0 1200 40" preserveAspectRatio="none" aria-hidden="true">
      <rect x="0" y="0" width="1200" height="40" fill="var(--brand-blue)"/>
      <polygon points="0,0 706,0 746,40 0,40" fill="var(--brand-green)"/>
    </svg>
  </section>

  <h2 class="services-label">OUR SERVICES</h2>

  <ul class="service service-fertiliser">
    <li class="service-title">FERTILISER SPREADING :</li>
    <li>Accurate, Pattern-tested equipment</li>
    <li>Zero crop damage or wheel marks</li>
    <li>Ability to load product out of a truck,<br>bin or bulk bags</li>
    <li>Prices from $32 per hectare depending<br>on spread rate</li>
  </ul>

  <ul class="service service-spraying">
    <li class="service-title">SPRAYING :</li>
    <li>Accurate</li>
    <li>Time Efficient</li>
    <li>Zero Crop damage</li>
    <li>Cost Efficient</li>
  </ul>

  <div class="brand-name"><span class="brand-dot"></span>Ridgeline Aviation</div>

  <svg class="band band-foot" viewBox="0 0 1200 22" preserveAspectRatio="none" aria-hidden="true">
    <rect x="0" y="0" width="600" height="22" fill="var(--brand-blue)"/>
    <rect x="600" y="0" width="600" height="22" fill="var(--brand-green)"/>
  </svg>
</main>
</body>
</html>
```